Simple+Professional tech feel + warm and friendly box design for pet test kit

Project Name: 10-Minute Canine & Feline Rapid Test Kit Packaging Design
Target Brand Reference: VELUMAR (South Korea) styles
Design Style Direction: Professional tech feel + warm and friendly
Professionalism (Professional): Clear typography and distinct information hierarchy to reflect the product’s scientific rigor and accuracy.
Technological: Reflected through clean graphics and a minimalist layout.
Friendly: Utilise soft, warm colour combinations to convey care for pets and well-wishes for their health.
International: The design should align with mainstream aesthetics and avoid cultural ambiguities.

Target Market(s)
European Union and the United States
Industry/Entity Type
Veterinary Medical
Look and feel
Each slider illustrates characteristics of the customer's brand and the style your logo design should communicate.

```html
<!DOCTYPE html>
<html lang="en">
<head>
<meta charset="utf-8">
<title>PawScan – Rapid Test Kit Dieline</title>
<link href="https://fonts.googleapis.com/css2?family=Montserrat:wght@500&family=Ubuntu:ital,wght@0,400;0,500;0,700;1,400&display=swap" rel="stylesheet">
<style>
  :root {
    --teal: #b2dbd7;
    --ink: #2c5a60;
    --orange: #f8a676;
    --panel: #f9f9f9;
    --cut: #2b2b2b;
    --paper: #ffffff;
    --photo-light: #eef0ee;
    --photo-mid: #c9cfc9;
  }
  html, body {
    margin: 0;
    padding: 0;
    width: 857px;
    height: 1200px;
    overflow: hidden;
    background: var(--paper);
  }
  .sheet {
    position: relative;
    width: 857px;
    height: 1200px;
  }
  .dieline {
    position: absolute;
    left: 23px;
    top: 370px;
    width: 811px;
    height: 461px;
  }
  .cut { stroke: var(--cut); stroke-width: 1.3; }
  .fill-teal { fill: var(--teal); }
  .fill-panel { fill: var(--panel); }
  .fill-orange { fill: var(--orange); }
  .wordmark {
    font-family: "Montserrat", sans-serif;
    font-weight: 500;
    fill: var(--ink);
  }
  .tm { font-family: "Ubuntu", sans-serif; font-size: 0.3em; }
  .text-ink { font-family: "Ubuntu", sans-serif; fill: var(--ink); }
  .text-white { font-family: "Ubuntu", sans-serif; fill: #ffffff; font-weight: 500; }
  .maker { font-family: "Ubuntu", sans-serif; fill: var(--ink); font-weight: 500; }
  .subtitle { font-weight: 400; }
  .tagline { font-style: italic; }
  .small { font-family: "Ubuntu", sans-serif; fill: var(--ink); font-size: 10px; }
  .tiny { font-family: "Ubuntu", sans-serif; fill: var(--ink); font-size: 8px; }
  .symbol { stroke: var(--ink); stroke-width: 1.4; fill: none; }
</style>
</head>
<body>
<main class="sheet">
  <svg class="dieline" viewBox="205 1383 1215 694" xmlns="http://www.w3.org/2000/svg">
    <defs>
      <radialGradient id="photo-tone" cx="50%" cy="45%" r="60%">
        <stop offset="0%" stop-color="var(--photo-light)"/>
        <stop offset="100%" stop-color="var(--photo-mid)"/>
      </radialGradient>
    </defs>

    <!-- Top tuck flap -->
    <path class="fill-panel cut" d="M205 1445 V1420 Q205 1385 240 1385 H580 Q615 1385 615 1420 V1445 Z"/>

    <!-- Top panel -->
    <g class="panel-top">
      <rect class="fill-panel cut" x="205" y="1445" width="410" height="198"/>
      <text class="wordmark" x="252" y="1558" font-size="40">PawScan<tspan class="tm" dy="-18">TM</tspan></text>
    </g>

    <!-- Back panel -->
    <g class="panel-back">
      <rect class="fill-panel" x="205" y="1643" width="410" height="192"/>
      <rect class="fill-teal" x="205" y="1835" width="410" height="8"/>
      <rect class="fill-orange" x="205" y="1843" width="410" height="74"/>
      <rect class="cut" fill="none" x="205" y="1643" width="410" height="274"/>
      <rect role="img" aria-label="Cat face line icon" fill="var(--ink)" opacity="0.18" x="243" y="1700" width="48" height="48" rx="10"/>
      <rect role="img" aria-label="Dog face line icon" fill="var(--ink)" opacity="0.18" x="300" y="1700" width="48" height="48" rx="10"/>
      <text class="wordmark" x="240" y="1818" font-size="40">PawScan<tspan class="tm" dy="-18">TM</tspan></text>
      <text class="maker" x="495" y="1810" font-size="19">Corvella</text>
      <text class="text-white" x="240" y="1886" font-size="18">5 Tests/Kit</text>
    </g>

    <!-- Bottom flap (back) -->
    <path class="fill-teal cut" d="M205 1917 H615 V2075 H560 Q540 2075 540 2055 V2015 H282 V2055 Q282 2075 262 2075 H205 Z"/>

    <!-- Left side panel -->
    <g class="panel-side-info">
      <path class="fill-teal cut" d="M615 1643 H622 L622 1565 Q622 1553 635 1553 H788 Q800 1553 800 1565 L805 1643 H812"/>
      <rect class="fill-teal cut" x="615" y="1643" width="197" height="274"/>
      <circle role="img" aria-label="Portrait photo of a white cat" cx="760" cy="1702" r="52" fill="url(#photo-tone)" stroke="#ffffff" stroke-width="3"/>
      <text class="wordmark" x="636" y="1767" font-size="18">PawScan<tspan class="tm" dy="-8">TM</tspan></text>
      <text class="small" x="636" y="1789">Corvella Biotech Limited</text>
      <text class="small" x="636" y="1803">Web:www.corvella-bio.com</text>
      <text class="small" x="636" y="1816">E-mail:sales@corvella-bio.com</text>
      <g class="storage-symbols">
        <circle class="symbol" cx="646" cy="1843" r="8"/>
        <text class="text-ink" x="642" y="1847" font-size="11" font-weight="700">2</text>
        <path class="symbol" d="M661 1842 Q670 1830 680 1842 Z M670 1842 V1852 Q670 1855 667 1854"/>
        <circle class="symbol" cx="696" cy="1843" r="4"/>
        <path class="symbol" d="M696 1833 V1836 M696 1850 V1853 M686 1843 H689 M703 1843 H706 M689 1836 L691 1838 M701 1848 L703 1850 M703 1836 L701 1838 M691 1848 L689 1850 M687 1852 L705 1834"/>
        <rect class="symbol" x="711" y="1835" width="28" height="16"/>
        <text class="text-ink" x="715" y="1847" font-size="9">IVD</text>
        <text class="tiny" x="744" y="1854">4°C</text>
        <path class="symbol" d="M765 1834 V1850"/>
        <circle cx="765" cy="1852" r="2.5" fill="var(--ink)"/>
        <text class="tiny" x="772" y="1842">30°C</text>
      </g>
      <text class="tiny" x="636" y="1878">(For accurate results, please read</text>
      <text class="tiny" x="636" y="1888">the instructions carefully before use)</text>
    </g>

    <!-- Bottom flap (left side) -->
    <path class="fill-teal cut" d="M615 1917 H812 V2052 H735 Q713 2052 713 2030 V1990 Z"/>

    <!-- Front panel -->
    <g class="panel-front">
      <rect class="fill-panel" x="812" y="1643" width="410" height="192"/>
      <rect class="fill-teal" x="812" y="1835" width="410" height="8"/>
      <rect class="fill-orange" x="812" y="1843" width="410" height="74"/>
      <rect class="cut" fill="none" x="812" y="1643" width="410" height="274"/>
      <text class="wordmark" x="846" y="1716" font-size="40">PawScan<tspan class="tm" dy="-18">TM</tspan></text>
      <text class="text-ink subtitle" x="848" y="1753" font-size="20">10-Minute Canine &amp;</text>
      <text class="text-ink subtitle" x="848" y="1780" font-size="20">Feline Rapid Test Kit</text>
      <text class="text-ink tagline" x="848" y="1808" font-size="15">For Dogs and Cats</text>
      <rect role="img" aria-label="Cat face line icon" fill="var(--ink)" opacity="0.18" x="1078" y="1735" width="50" height="50" rx="10"/>
      <rect role="img" aria-label="Dog face line icon" fill="var(--ink)" opacity="0.18" x="1136" y="1735" width="50" height="50" rx="10"/>
      <text class="text-white" x="848" y="1886" font-size="18">5 Tests/Kit</text>
      <text class="text-white" x="1100" y="1886" font-size="18">Corvella</text>
    </g>

    <!-- Bottom flap (front) -->
    <path class="fill-teal cut" d="M812 1917 H1222 L1145 2015 V2055 Q1145 2075 1125 2075 H908 Q888 2075 888 2055 V2015 Z"/>

    <!-- Right side panel -->
    <g class="panel-side-story">
      <path class="fill-teal cut" d="M1222 1643 H1228 L1235 1565 Q1236 1553 1248 1553 H1410 V1643 H1418"/>
      <rect class="fill-teal cut" x="1222" y="1643" width="196" height="274"/>
      <text class="wordmark" x="1247" y="1732" font-size="18">PawScan<tspan class="tm" dy="-8">TM</tspan></text>
      <text class="small" x="1247" y="1756">is made by Corvella, our name</text>
      <text class="small" x="1247" y="1768">combines 'Cor' for the heart</text>
      <text class="small" x="1247" y="1780">with "Vella" for clear vision,</text>
      <text class="small" x="1247" y="1792">representing both intelligent</text>
      <text class="small" x="1247" y="1804">efficacy in our science and</text>
      <text class="small" x="1247" y="1816">reverence for the spirit of life</text>
      <text class="small" x="1247" y="1828">('Care for Every Life') in all</text>
      <text class="small" x="1247" y="1840">creatures.</text>
    </g>

    <!-- Bottom flap (right side) -->
    <path class="fill-teal cut" d="M1222 1917 H1418 L1320 1990 V2030 Q1320 2052 1298 2052 H1222 Z"/>
  </svg>
</main>
</body>
</html>
```